TeamForge - Re-work of the attached flyer

graphical improvements and professionalism

Target Market(s)

European corporates like KL, Velmar, Quelidon

Industry/Entity Type

Work

Font styles to use
Sans Serif

Colors

Designer to choose colors to be used in the design.

Requirements
Must have
• must be compelling and attract the readers attantion
Nice to have
• Metaphore: The Wave is the Disruptive Innovation rolling towards us - the surfer is the corporate trying to master the change
Should not have
• should not be boaring

```html
<!DOCTYPE html>
<html lang="de">
<head>
<meta charset="utf-8">
<title>TeamForge – Disruptive Innovation Factory Flyer</title>
<link href="https://fonts.googleapis.com/css2?family=Montserrat:wght@400;500;600;700&family=Raleway:wght@400;500&family=Oswald:wght@400;500&display=swap" rel="stylesheet">
<style>
:root{
  --navy:#1c1f4f;
  --navy-deep:#14173d;
  --gold:#c5a63e;
  --gold-pale:#e6dcb8;
  --ink:#2b2b2b;
  --panel:#f0f0f1;
  --paper:#ffffff;
  --stage:#d7d7da;
  --sea-dark:#1b4e78;
  --sea-light:#bfe0ee;
}
*{margin:0;padding:0;box-sizing:border-box}
html,body{width:1200px;height:1200px;overflow:hidden;background:var(--stage)}
.canvas{position:relative;width:1200px;height:1200px}
.sheet{position:absolute;width:951px;height:672px;transform:scale(.8);transform-origin:0 0;overflow:hidden;background:var(--paper);box-shadow:0 4px 14px rgba(0,0,0,.25)}
.sheet--front{left:38px;top:66px}
.sheet--back{left:401px;top:630px}
.sheet svg.bg{position:absolute;left:0;top:0;width:951px;height:672px}
.abs{position:absolute}
.head{font-family:Montserrat,sans-serif;font-weight:600;font-size:11px;line-height:1.3;color:var(--navy-deep);text-transform:uppercase}
.body{font-family:Raleway,sans-serif;font-size:7.7px;line-height:1.4;color:var(--ink)}
.body p{margin-bottom:9px}
.footer{font-family:Montserrat,sans-serif;color:var(--navy);text-align:center}
.brand-seal{position:absolute;left:702px;top:98px;width:170px;height:170px;border-radius:50%;background:var(--navy);border:5px solid var(--paper);display:flex;align-items:center;justify-content:center}
.brand-seal span{font-family:Montserrat,sans-serif;font-weight:600;font-size:22px;color:var(--paper)}
.back-title{left:0;top:30px;width:951px;text-align:center;font-family:Montserrat,sans-serif;font-weight:600;font-size:20px;line-height:1.3;color:var(--paper)}
.stage{font-family:Montserrat,sans-serif;font-weight:600;font-size:7px;fill:var(--paper)}
.box-label{font-family:Oswald,sans-serif;font-size:8px;fill:var(--paper)}
.axis-label{font-family:Montserrat,sans-serif;font-weight:600;font-size:13px;line-height:1;color:var(--gold);text-align:center}
.caption{font-family:Montserrat,sans-serif;font-size:10px;line-height:1.2;color:var(--paper);text-align:center}
.delivery{font-family:Montserrat,sans-serif;font-weight:600;font-size:14px;color:var(--gold)}
.diagram-claim{font-family:Montserrat,sans-serif;font-weight:600;font-size:10px;line-height:1.15;color:var(--paper);text-align:center}
.manifesto{font-family:Montserrat,sans-serif;font-weight:600;font-size:13px;color:var(--navy)}
.back .body{color:var(--navy-deep)}
</style>
</head>
<body>
<div class="canvas">

  <section class="sheet sheet--front">
    <svg class="bg" viewBox="0 0 951 672">
      <defs>
        <linearGradient id="sea" x1="0" y1="0" x2="1" y2="0.4">
          <stop offset="0" stop-color="var(--sea-dark)"/>
          <stop offset=".55" stop-color="#3f86a8"/>
          <stop offset="1" stop-color="var(--sea-light)"/>
        </linearGradient>
      </defs>
      <rect x="320" y="0" width="310" height="672" fill="var(--panel)"/>
      <path role="img" aria-label="Foto: Surfer reitet eine mächtige Welle" fill="url(#sea)"
        d="M0,0 H951 V105 C860,120 760,165 650,180 C580,190 480,185 380,165 C260,140 140,105 0,100 Z"/>
      <path fill="var(--navy)"
        d="M0,100 C140,105 260,140 380,165 C480,185 580,190 650,180 C760,165 860,120 951,105 V215 C860,210 760,212 640,200 C540,190 430,165 330,155 C250,150 100,165 0,175 Z"/>
      <path fill="var(--gold)"
        d="M330,155 C430,165 540,190 640,200 C760,212 860,210 951,215 V283 C870,275 780,260 680,250 C560,235 450,200 330,155 Z"/>
      <path fill="var(--gold)" d="M630,672 V628 C700,610 800,600 951,610 V672 Z"/>
      <path fill="var(--navy)" d="M630,632 C700,610 800,598 951,606 V614 C800,606 700,616 630,640 Z"/>
    </svg>

    <div class="brand-seal"><span>TeamForge</span></div>

    <h2 class="abs head" style="left:132px;top:225px;width:170px">Disruptive Innovation<br>Factory (DIF)</h2>
    <div class="abs body" style="left:20px;top:262px;width:290px">
      <p style="padding-left:40px">In diesen Jahren stellen wir überall fest, dass die vierte industrielle Revolution die Digitalisierung von Märkten und Prozessen in vollem Gange nimmt. Wir stehen am Beginn einer neuen Ära der globalen Kollaboration und des Wettbewerbs.</p>
      <p>Digitale Technologien, etwa die weltweite Vernetzung von Daten und Information, werden bis 2025 eine Milliarde neuer Nutzer verbinden. Eine Billion Geräte und Maschinen liefern bis 2030 über Sensoren aktuelle Messdaten rund um die Uhr. Information wird «zeitlos» und «grenzenlos».</p>
      <p>Der sich heute abzeichnende Ausstieg aus dem technologischen Paradigma fossiler Brennstoffe sowie das Fortschreiten der Digitalisierung ganzer Prozessketten hat die Neu-Definition traditioneller Geschäftsmodelle zur Folge.</p>
      <p>Jedes wirtschaftlich agierende Unternehmen, ganz egal wie gross oder klein, wird sich in den nächsten Jahren im Zuge der digitalisierten Geschäftswelt neu „erfinden“ müssen. Dabei ist Grösse, Historie und früher erworbene Marktmacht nur marginal.</p>
      <p>Diese Veränderungen in einer „Digitalisierten Industrie und Geschäftswelt“ haben einen signifikanten Einfluss auf die zukünftige Entwicklung jedes Unternehmens – auch des Ihren.</p>
      <p>Die gute Nachricht: Wir haben nicht die vordefinierten Antworten auf alle Ihre Fragen – aber wir haben die Methode, die Experten, die Werkzeuge und die Erfahrung, um mit Ihnen die richtigen Antworten auf die sich Ihnen stellenden Herausforderungen zu finden.</p>
    </div>

    <h2 class="abs head" style="left:335px;top:232px;width:200px">Pivoting corporates from<br>“final destination” to<br>“exponential acceleration”</h2>
    <div class="abs body" style="left:335px;top:290px;width:282px">
      <p>Das DIF-Prinzip: Nach den Regeln der agilen Projektmethodik reflektieren und hinterfragen Sie in Ihrem Unternehmen installierte Geschäftsprozesse und herrschende Paradigmen. Sie stellen innerhalb des Prozesses die Durchführung einer „DIF“, die Geschäftsmodelle und herrschenden Überzeugungen Ihres Unternehmens in Frage. In theoretischen Szenarios „zerstören“ Sie Ihr eigenes Wirken samt Kerngeschäft, um es anschliessend für die digitalisierte Realität neu zu definieren und zu erfinden.</p>
      <p>Das Vorgehen: Ausgewählte Mitarbeitende werden zunächst mit den agilen Methoden und Denkansätzen der „Disruptive Innovation Factory“ befähigt und definieren im zweiten Schritt, in Kollaboration mit erfahrenen Projekt-Managern und Business Coaches, umsetzbare digitalisierte Innovationen für Ihre Produkte und Dienstleistungen.</p>
      <p>Das Ziel: Nicht weniger als die exponentiell wachsende Fortentwicklung Ihres Unternehmens in der Ära der digitalen Realität.</p>
      <p>Das Risiko ist unser aller Chance:</p>
      <p>In unserer Ära haben wir die Wahl: Entweder wir definieren unsere Kerngeschäfte, Prozesse und Paradigmen vor dem Hintergrund globalisierter und vernetzter Möglichkeiten neu – oder ein anderer Marktteilnehmer tut es für uns.</p>
    </div>
    <p class="abs footer" style="left:335px;top:646px;width:280px;font-size:7.5px;font-weight:600">Copyright© TeamForge™ Consulting &amp; Coaching LLC</p>

    <h2 class="abs head" style="left:650px;top:296px;width:280px;text-align:center">Disruptive Innovation und<br>was das bedeutet…</h2>
    <div class="abs body" style="left:643px;top:332px;width:290px">
      <p>Sie haben nicht unrecht, wenn Sie sagen: «Disruptive Innovation» hat es schon immer gegeben – das ist doch eigentlich nichts wirklich Neues. Der Traktor war »disruptive« für den Knecht auf dem Bauernhof, das Automobil für die Pferdekutschen.</p>
      <p>Im Unterschied zu diesen ersten industriellen »Revolutionen« jedoch schreitet die vierte industrielle Revolution mit rasender Geschwindigkeit und fundamentalen Veränderungen bei der Kooperation von Unternehmensprozessen voran. Die Anforderungen an die permanente Veränderungsfähigkeit sind im «normalen» Arbeitsmodus eines Unternehmens nicht zu bewältigen.</p>
      <p>Die kontinuierliche, methodenbasierte Auseinandersetzung mit sich permanent verändernden Marktbedingungen muss zwingend dem «Gen-Pool» jedes Unternehmens hinzugefügt werden. Das Unternehmen muss sich befähigen, in einer VUCA-Welt konkurrenzfähig zu werden und zu bleiben.</p>
      <p>Die Implementierung der unternehmenseigenen «DFI» versetzt ein Corporate-Unternehmen in die Lage, im globalen Wettbewerb mit kompetitiven und innovativen «Start-ups» zu bestehen.</p>
    </div>
    <div class="abs footer" style="left:630px;top:618px;width:320px">
      <p style="font-size:9px;font-weight:600">TeamForge™ Consulting &amp; Coaching LLC</p>
      <p style="font-size:7.5px;color:var(--paper);margin-top:6px">⌖ Seeblickweg 7 CH 6000 Uferdorf / LU</p>
      <p style="font-size:6.5px;color:var(--paper);margin-top:4px">✆ +41 41 555 01 10 &nbsp;&nbsp; ✉ office@teamforge-tf.com<br>+41 79 555 02 20 &nbsp;&nbsp; ◍ www.TeamForge-tf.com</p>
    </div>
  </section>

  <section class="sheet sheet--back back">
    <svg class="bg" viewBox="0 0 951 672">
      <defs>
        <linearGradient id="surf" x1="0" y1="0" x2="1" y2="0.6">
          <stop offset="0" stop-color="#4a4c55"/>
          <stop offset=".45" stop-color="#9a9ca3"/>
          <stop offset="1" stop-color="#eeeef0"/>
        </linearGradient>
      </defs>
      <rect role="img" aria-label="Foto: brechende Welle mit Surfer in Graustufen" width="951" height="672" fill="url(#surf)"/>
      <path fill="var(--gold)" d="M0,0 H951 V95 C800,120 650,165 480,165 C300,165 150,170 0,210 Z"/>
      <path fill="var(--navy)" d="M0,210 C150,170 300,165 480,165 C650,165 800,120 951,95 V160 C820,150 700,175 560,200 C420,225 260,195 140,220 C80,232 30,250 0,265 Z"/>
      <path fill="var(--gold)" d="M260,185 C360,160 440,180 520,205 C640,240 760,225 951,210 V238 C780,238 650,250 520,230 C430,216 340,190 260,185 Z"/>

      <path d="M282,520 V248" stroke="var(--gold)" stroke-width="2.5"/>
      <path d="M275,252 L282,238 L289,252 Z" fill="var(--gold)"/>
      <path d="M282,518 H740" stroke="var(--gold)" stroke-width="2.5"/>
      <path d="M738,511 L752,518 L738,525 Z" fill="var(--gold)"/>

      <path d="M314,250 H398 L408,265 L398,280 H314 Z" fill="var(--navy)"/>
      <path d="M398,250 H484 L494,265 L484,280 H398 L408,265 Z" fill="var(--navy)"/>
      <path d="M484,250 H565 L575,265 L565,280 H484 L494,265 Z" fill="var(--navy)"/>
      <path d="M565,250 H648 L658,265 L648,280 H565 L575,265 Z" fill="var(--gold)"/>
      <path d="M648,250 H750 L760,265 L750,280 H648 L658,265 Z" fill="var(--gold-pale)"/>
      <text class="stage" x="356" y="268" text-anchor="middle">DIAGNOSE</text>
      <text class="stage" x="442" y="268" text-anchor="middle">FOKUSSIERUNG</text>
      <text class="stage" x="525" y="268" text-anchor="middle">VALIDIERUNG</text>
      <text class="stage" x="608" y="268" text-anchor="middle">ABNAHME</text>
      <text class="stage" x="705" y="268" text-anchor="middle">MOBILISIERUNG</text>

      <rect x="315" y="280" width="440" height="160" fill="var(--gold)" opacity=".92"/>

      <rect x="332" y="352" width="94" height="42" fill="var(--navy)"/>
      <rect x="432" y="352" width="92" height="42" fill="var(--navy)"/>
      <rect x="532" y="352" width="92" height="42" fill="var(--navy)"/>
      <rect x="632" y="352" width="92" height="42" fill="var(--navy)"/>
      <text class="box-label" x="379" y="376" text-anchor="middle">NLP</text>
      <text class="box-label" x="478" y="376" text-anchor="middle">NVC</text>
      <text class="box-label" x="578" y="376" text-anchor="middle">SIXSIGMA</text>
      <text class="box-label" x="678" y="376" text-anchor="middle">…</text>

      <rect x="320" y="396" width="135" height="44" fill="var(--navy)"/>
      <rect x="458" y="396" width="110" height="44" fill="var(--navy)"/>
      <rect x="610" y="396" width="135" height="44" fill="var(--navy)"/>
      <text class="box-label" x="332" y="414">DESIGN</text>
      <text class="box-label" x="332" y="425">THINKING</text>
      <g fill="var(--paper)">
        <circle cx="384" cy="418" r="4"/><circle cx="396" cy="418" r="5"/><circle cx="409" cy="418" r="5.5"/>
        <circle cx="422" cy="418" r="5"/><circle cx="435" cy="418" r="4"/>
      </g>
      <text class="box-label" x="490" y="421" text-anchor="middle">SCRUM</text>
      <path d="M535,430 A11,11 0 1 1 548,424" fill="none" stroke="var(--paper)" stroke-width="2"/>
      <path d="M545,420 L551,425 L544,428 Z" fill="var(--paper)"/>
      <text class="box-label" x="617" y="414">LEAN MANAGEMENT</text>
      <text class="box-label" x="617" y="425">(KANBAN)</text>
      <g fill="none" stroke="var(--paper)" stroke-width="1.2">
        <rect x="703" y="406" width="36" height="26"/>
        <path d="M712,406 V432 M721,406 V432 M730,406 V432"/>
      </g>
    </svg>

    <h1 class="abs back-title">AGILE PM-METHODEN BILDEN ZUSAMMEN DIE BOOSTER IM<br>PROZESS DER “DISRUPTIVE INNOVATION FACTORY”</h1>

    <p class="abs diagram-claim" style="left:315px;top:290px;width:440px">INNOVATIONSKRAFT AKTIVIEREN, FÄHIGKEITEN VERMITTELN, KULTUR FORMEN,<br>FOCUS AUF WACHSTUM UND PROFIT LEGEN</p>
    <p class="abs manifesto" style="left:405px;top:328px">AGILE MANIFESTO</p>

    <p class="abs axis-label" style="left:175px;top:354px;width:90px">MINDSET<br>und<br>VALUES</p>
    <p class="abs axis-label" style="left:175px;top:437px;width:90px">PROZESS/<br>METHODE</p>

    <p class="abs caption" style="left:290px;top:473px;width:140px">Customer-oriented<br>ideation and innovation</p>
    <p class="abs caption" style="left:465px;top:473px;width:140px">Development of new<br>products &amp; services</p>
    <p class="abs caption" style="left:625px;top:473px;width:150px">Optimization of existing<br>solutions and processes</p>

    <p class="abs delivery" style="left:295px;top:524px">SOLUTION GENERATION</p>
    <p class="abs delivery" style="left:620px;top:524px">EFFICIENT DELIVERY</p>

    <div class="abs body" style="left:26px;top:558px;width:285px">
      <p>Die «Disruptive Innovation Factory (DIF)» folgt einem vordefinierten agilen Implementierungsprozess. Das erklärte Ziel des DIF-Prozesses ist es, Ihr Corporate-Unternehmen zur proaktiven Teilnahme und Gestaltung in der Ära der Disruption (Digitalen) Innovation zu befähigen. Beginnend (1.) mit der Selektion der Mitglieder der zukünftigen DIF aus dem Kreis der Mitarbeitenden in Ihrem Unternehmen und deren Vorbereitung auf die Aufgaben</p>
    </div>
    <div class="abs body" style="left:339px;top:558px;width:285px">
      <p>in der DIF werden wir (2.) mit der methodischen Befähigung und Qualifikation der selektierten Prozess-Innovatoren im Rahmen von definierten Workshops beginnen. Die theoretischen Grundlagen und Praxiserfahrungen werden im Kontext Ihres Unternehmens (3.) auf Ihre Handlungsschwerpunkte angewandt – der Disruptive Innovationsprozess auf Ihr definiertes Handlungsfeld nimmt seine Arbeit auf. In Teams (4.) werden mittels</p>
    </div>
    <div class="abs body" style="left:643px;top:558px;width:285px">
      <p>des iterativen DIF-Prozesses (z.B. Design Thinking) werden unterschiedliche Konzeptionen und Innovationskonzepte erstellt und in Form von Business-Modellen / Business Cases dem Management zur Umsetzung und Implementierung vorgeschlagen. Wichtig: Das Ziel der DIF, den in Ihrem Unternehmen vorhandenen Genius zur kreativen Innovation zu adressieren – bei den folgenden Schritten begleiten wir Sie mit weiteren TeamForge™ Consulting &amp; Coaching Formaten.</p>
    </div>
  </section>

</div>
</body>
</html>
```